Business Card Design Project

Attached is a rough business card design. We like this general design but we feel that the layout, text, color can use improvement and we seek the help of a professional designer.
We have a television and film production company based in New York. We need our cards for television network executives, other production executives, financiers etc. We deal with creative types as well as business people so we need the card to be interesting and edgy just like the name of our company - KICKTHEDOOR. The design should reflect the edgy, punk rock attitude of our company.
We prefer orange typeface for the logo but we're open to other ideas. I am attaching our existing business card and other files to help with the design.
Thank you in advance!!
Updates
Target Market(s)
Television and film producers, television network executives, other production executives, financiers, distribution companies
Industry/Entity Type
Film Production
Requirements
Must have
- I am attaching a photo of the company mascot which is a dog. We prefer to have the dog's photo as part of the card but we're open to the other ideas.
Name, phone number, email

```html
<!DOCTYPE html>
<html lang="en">
<head>
<meta charset="utf-8">
<title>Kickthedoor business card</title>
<link rel="stylesheet" href="https://fonts.googleapis.com/css2?family=Poppins:wght@400;800&display=swap">
<style>
  :root {
    --card-white: #ffffff;
    --ink: #111111;
    --brand-orange: #f26a1b;
    --frame: #0b0b0b;
    --backdrop-dark: #2a1d24;
    --backdrop-plum: #6b4a5a;
    --mascot-deep: #7a4a3c;
    --mascot-mid: #c98a6c;
    --mascot-light: #ecc2a6;
    --mascot-blush: #f6e0dc;
  }
  * { margin: 0; padding: 0; box-sizing: border-box; }
  html, body {
    width: 1200px;
    height: 686px;
    overflow: hidden;
    background: var(--frame);
  }
  .business-card {
    position: relative;
    width: 1200px;
    height: 686px;
    background: var(--card-white);
    overflow: hidden;
    font-family: "Poppins", "Century Gothic", sans-serif;
    color: var(--ink);
  }
  .mascot-photo {
    position: absolute;
    top: 0;
    right: 0;
    width: 640px;
    height: 686px;
    background:
      radial-gradient(ellipse 38% 30% at 60% 92%, var(--mascot-deep) 0%, rgba(122,74,60,0) 75%),
      radial-gradient(ellipse 52% 46% at 68% 58%, var(--mascot-mid) 0%, rgba(201,138,108,0) 72%),
      radial-gradient(ellipse 60% 26% at 78% 8%, var(--backdrop-dark) 0%, var(--backdrop-plum) 45%, rgba(107,74,90,0) 100%),
      linear-gradient(90deg, rgba(255,255,255,1) 0%, var(--mascot-blush) 14%, var(--mascot-light) 34%, var(--mascot-mid) 70%, var(--mascot-deep) 100%);
  }
  .brand-name {
    position: absolute;
    left: 84px;
    top: 50px;
    font-size: 62px;
    font-weight: 800;
    line-height: 1;
    letter-spacing: -1px;
    color: var(--brand-orange);
  }
  .contact-details {
    position: absolute;
    left: 82px;
    top: 318px;
    list-style: none;
  }
  .contact-details li {
    font-size: 35px;
    font-weight: 400;
    line-height: 1;
    letter-spacing: 1.5px;
    height: 114px;
    white-space: nowrap;
  }
  .contact-details .phone { letter-spacing: 3.5px; }
  .contact-details .email { letter-spacing: 1px; }
  .card-frame {
    position: absolute;
    inset: 0;
    pointer-events: none;
    box-shadow:
      inset 0 0 0 7px var(--frame),
      inset 0 0 16px 10px rgba(11,11,11,0.85);
  }
</style>
</head>
<body>
  <div class="business-card">
    <div class="mascot-photo" role="img" aria-label="Photo of the company mascot, a bulldog resting its head on a small soccer ball"></div>
    <div class="brand-name">kickthedoor</div>
    <ul class="contact-details">
      <li class="person-name">Marco Delgado</li>
      <li class="phone">917-555-0148</li>
      <li class="email">marco@kickthedoor.com</li>
    </ul>
    <div class="card-frame"></div>
  </div>
</body>
</html>
```